Design für einen Jahresplaner gesucht
Zielgruppe
Scannen und Designen Zahntechnischer und Zahnmedizinischer Arbeiten und das Fräsen und 3d Drucken von bereits in CAD konstruierten Objekten. Wir verfügen über die modernsten Zahntechnischen Technologien und bieten diese als Dienstleister für Dentallabore an.
Aufgabenstellung
Wir benotigen ein Jahresplaner für unsere Kunden. Die Beigefügte Vorlage dient regelrecht nur der Grösenvorlage.
Das Design soll Technisch und Innovativ sein. Gleischzeitig aber gradlinig und nicht zu verspielt.
Das Logo kann ruhig stark ins Auge fallen. Die Schriftfarben sollen überwigen dunkelgrau sein. Hervorzuhebende Bereiche wie z. B. Sonntage, Feiertage sollten die Logofaben beinhalten. Bilder können auch verwendet werden aber wir würden uns über ein Schönes Layout ohne Bilder auch freuen.
PS: Unter dem Logo muss in Feiner Schrift stehen
eine Marke der Norvak GmbH

```html
<!DOCTYPE html>
<html lang="de">
<head>
<meta charset="utf-8">
<title>Jahresplaner 2019 – Dentora</title>
<link href="https://fonts.googleapis.com/css2?family=Open+Sans:wdth,wght@75..100,300..800&display=swap" rel="stylesheet">
<style>
  :root {
    --bg: #2b2a29;
    --blue: #2394d3;
    --magenta: #a22a87;
    --holiday: #f8d48e;
    --weekend: #dcdcdc;
    --cell: #ffffff;
    --ink: #2b2a29;
    --label: #f0f0f0;
    --year: #666666;
  }
  * { margin: 0; padding: 0; box-sizing: border-box; }
  html, body { width: 1200px; height: 840px; overflow: hidden; background: var(--bg); }
  body { font-family: "Open Sans", Arial, sans-serif; color: var(--ink); }
  .planner { position: relative; width: 1200px; height: 840px; background: var(--bg); overflow: hidden; }
  .year {
    position: absolute; left: 536px; top: 22px;
    font-size: 106px; font-weight: 400; color: var(--year); letter-spacing: 2px; line-height: 1;
  }
  .month { position: absolute; left: 0; width: 1200px; height: 80px; }
  .month h2 {
    position: absolute; right: 1088px; top: 33px;
    font-size: 15px; font-weight: 700; font-stretch: 80%; color: #fff; letter-spacing: 0.2px;
  }
  .weekdays, .days {
    position: absolute; left: 120px; list-style: none;
    display: grid; grid-template-columns: repeat(31, 31px); column-gap: 1.95px;
  }
  .weekdays { top: 0; }
  .weekdays li { text-align: center; font-size: 14px; font-weight: 300; color: var(--label); line-height: 16px; }
  .weekdays li.off { color: #777; }
  .days { top: 16px; }
  .days li { position: relative; height: 60px; background: var(--cell); text-align: center; }
  .days b { display: block; padding-top: 4px; font-size: 20px; font-weight: 400; font-stretch: 92%; line-height: 24px; color: var(--ink); }
  .days .w { background: var(--weekend); }
  .days .h { background: var(--holiday); }
  .days .w b, .days .h b { color: var(--blue); font-weight: 700; }
  .days .x { background: transparent; border: 1px solid #9a9a9a; }
  .days i {
    position: absolute; left: 1px; top: 1px;
    font-style: normal; font-size: 6.5px; font-weight: 700; color: var(--magenta); line-height: 1;
  }
  .days small {
    position: absolute; left: 0; right: 0; bottom: 4px;
    font-size: 5px; font-weight: 700; font-stretch: 75%; line-height: 6px; color: #555; text-transform: uppercase;
  }
  .days small.light { font-weight: 400; color: #777; }
  .jan { top: 152px; } .feb { top: 242px; } .mar { top: 332px; }
  .apr { top: 422px; } .mai { top: 512px; } .jun { top: 602px; }
  .claim {
    position: absolute; left: 342px; top: 713px;
    font-size: 12px; line-height: 16.3px; letter-spacing: 2.3px; color: #8a8a8a; font-weight: 400;
  }
  .mesh-visual {
    position: absolute; left: 862px; top: 685px; width: 320px; height: 135px;
    background: radial-gradient(ellipse at 55% 50%, rgba(120,120,130,0.35), rgba(80,80,90,0.12) 60%, rgba(43,42,41,0) 80%);
  }
  .brand { position: absolute; left: 724px; top: 722px; }
  .brand-name { font-size: 62px; font-weight: 700; color: #666; line-height: 1; letter-spacing: -1px; }
  .brand-dot { position: absolute; left: -30px; top: 24px; width: 18px; height: 18px; border-radius: 50%; background: var(--blue); }
  .brand-sub { position: absolute; left: 3px; top: 70px; white-space: nowrap; font-size: 16.5px; font-weight: 300; color: #777; letter-spacing: 0.6px; }
</style>
</head>
<body>
<main class="planner">
  <h1 class="year">2019</h1>

  <section class="month jan">
    <h2>JANUAR</h2>
    <ol class="weekdays"><li>di</li><li>mi</li><li>do</li><li>fr</li><li>sa</li><li>so</li><li>mo</li><li>di</li><li>mi</li><li>do</li><li>fr</li><li>sa</li><li>so</li><li>mo</li><li>di</li><li>mi</li><li>do</li><li>fr</li><li>sa</li><li>so</li><li>mo</li><li>di</li><li>mi</li><li>do</li><li>fr</li><li>sa</li><li>so</li><li>mo</li><li>di</li><li>mi</li><li>do</li></ol>
    <ol class="days">
      <li class="h"><i>01</i><b>01</b><small>Neujahr</small></li><li><b>02</b></li><li><b>03</b></li><li><b>04</b></li><li class="w"><b>05</b></li><li class="w"><b>06</b><small>Heilige<br>Drei<br>Könige</small></li>
      <li><i>02</i><b>07</b></li><li><b>08</b></li><li><b>09</b></li><li><b>10</b></li><li><b>11</b></li><li class="w"><b>12</b></li><li class="w"><b>13</b></li>
      <li><i>03</i><b>14</b></li><li><b>15</b></li><li><b>16</b></li><li><b>17</b></li><li><b>18</b></li><li class="w"><b>19</b></li><li class="w"><b>20</b></li>
      <li><i>04</i><b>21</b></li><li><b>22</b></li><li><b>23</b></li><li><b>24</b></li><li><b>25</b></li><li class="w"><b>26</b></li><li class="w"><b>27</b></li>
      <li><i>05</i><b>28</b></li><li><b>29</b></li><li><b>30</b></li><li><b>31</b></li>
    </ol>
  </section>

  <section class="month feb">
    <h2>FEBRUAR</h2>
    <ol class="weekdays"><li>fr</li><li>sa</li><li>so</li><li>mo</li><li>di</li><li>mi</li><li>do</li><li>fr</li><li>sa</li><li>so</li><li>mo</li><li>di</li><li>mi</li><li>do</li><li>fr</li><li>sa</li><li>so</li><li>mo</li><li>di</li><li>mi</li><li>do</li><li>fr</li><li>sa</li><li>so</li><li>mo</li><li>di</li><li>mi</li><li>do</li><li class="off">fr</li><li class="off">sa</li><li class="off">so</li></ol>
    <ol class="days">
      <li><i>05</i><b>01</b></li><li class="w"><b>02</b></li><li class="w"><b>03</b></li>
      <li><i>06</i><b>04</b></li><li><b>05</b></li><li><b>06</b></li><li><b>07</b></li><li><b>08</b></li><li class="w"><b>09</b></li><li class="w"><b>10</b></li>
      <li><i>07</i><b>11</b></li><li><b>12</b></li><li><b>13</b></li><li><b>14</b></li><li><b>15</b></li><li class="w"><b>16</b></li><li class="w"><b>17</b></li>
      <li><i>08</i><b>18</b></li><li><b>19</b></li><li><b>20</b></li><li><b>21</b></li><li><b>22</b></li><li class="w"><b>23</b></li><li class="w"><b>24</b></li>
      <li><i>09</i><b>25</b></li><li><b>26</b></li><li><b>27</b></li><li><b>28</b></li>
      <li class="x"></li><li class="x"></li><li class="x"></li>
    </ol>
  </section>

  <section class="month mar">
    <h2>MÄRZ</h2>
    <ol class="weekdays"><li>fr</li><li>sa</li><li>so</li><li>mo</li><li>di</li><li>mi</li><li>do</li><li>fr</li><li>sa</li><li>so</li><li>mo</li><li>di</li><li>mi</li><li>do</li><li>fr</li><li>sa</li><li>so</li><li>mo</li><li>di</li><li>mi</li><li>do</li><li>fr</li><li>sa</li><li>so</li><li>mo</li><li>di</li><li>mi</li><li>do</li><li>fr</li><li>sa</li><li>so</li></ol>
    <ol class="days">
      <li><i>09</i><b>01</b></li><li class="w"><b>02</b></li><li class="w"><b>03</b></li>
      <li><i>10</i><b>04</b><small>Rosen<br>Montag</small></li><li><b>05</b><small>Fastnacht</small></li><li><b>06</b><small>Ascher<br>Mittwoch</small></li><li><b>07</b></li><li><b>08</b></li><li class="w"><b>09</b></li><li class="w"><b>10</b></li>
      <li><i>11</i><b>11</b></li><li><b>12</b></li><li><b>13</b></li><li><b>14</b></li><li><b>15</b></li><li class="w"><b>16</b></li><li class="w"><b>17</b></li>
      <li><i>12</i><b>18</b></li><li><b>19</b></li><li><b>20</b><small class="light">Frühlings<br>Anfang</small></li><li><b>21</b></li><li><b>22</b></li><li class="w"><b>23</b></li><li class="w"><b>24</b></li>
      <li><i>13</i><b>25</b></li><li><b>26</b></li><li><b>27</b></li><li><b>28</b></li><li><b>29</b></li><li class="w"><b>30</b></li><li class="w"><b>31</b><small class="light">Beginn der<br>Sommerzeit</small></li>
    </ol>
  </section>

  <section class="month apr">
    <h2>APRIL</h2>
    <ol class="weekdays"><li>mo</li><li>di</li><li>mi</li><li>do</li><li>fr</li><li>sa</li><li>so</li><li>mo</li><li>di</li><li>mi</li><li>do</li><li>fr</li><li>sa</li><li>so</li><li>mo</li><li>di</li><li>mi</li><li>do</li><li>fr</li><li>sa</li><li>so</li><li>mo</li><li>di</li><li>mi</li><li>do</li><li>fr</li><li>sa</li><li>so</li><li>mo</li><li>di</li><li class="off">mi</li></ol>
    <ol class="days">
      <li><i>14</i><b>01</b></li><li><b>02</b></li><li><b>03</b></li><li><b>04</b></li><li><b>05</b></li><li class="w"><b>06</b></li><li class="w"><b>07</b></li>
      <li><i>15</i><b>08</b></li><li><b>09</b></li><li><b>10</b></li><li><b>11</b></li><li><b>12</b></li><li class="w"><b>13</b></li><li class="w"><b>14</b><small>Palm<br>Sonntag</small></li>
      <li><i>16</i><b>15</b></li><li><b>16</b></li><li><b>17</b></li><li><b>18</b><small>Grün<br>Donners<br>Tag</small></li><li class="h"><b>19</b><small>Kar<br>Freitag</small></li><li class="w"><b>20</b></li><li class="h"><b>21</b><small>Oster<br>Sonntag</small></li>
      <li class="h"><i>17</i><b>22</b><small>Oster<br>Montag</small></li><li><b>23</b></li><li><b>24</b></li><li><b>25</b></li><li><b>26</b></li><li class="w"><b>27</b></li><li class="w"><b>28</b></li>
      <li><i>18</i><b>29</b></li><li><b>30</b></li><li class="x"></li>
    </ol>
  </section>

  <section class="month mai">
    <h2>MAI</h2>
    <ol class="weekdays"><li>mi</li><li>do</li><li>fr</li><li>sa</li><li>so</li><li>mo</li><li>di</li><li>mi</li><li>do</li><li>fr</li><li>sa</li><li>so</li><li>mo</li><li>di</li><li>mi</li><li>do</li><li>fr</li><li>sa</li><li>so</li><li>mo</li><li>di</li><li>mi</li><li>do</li><li>fr</li><li>sa</li><li>so</li><li>mo</li><li>di</li><li>mi</li><li>do</li><li>fr</li></ol>
    <ol class="days">
      <li class="h"><i>18</i><b>01</b></li><li><b>02</b></li><li><b>03</b></li><li class="w"><b>04</b></li><li class="w"><b>05</b></li>
      <li><i>19</i><b>06</b></li><li><b>07</b></li><li><b>08</b></li><li><b>09</b></li><li><b>10</b></li><li class="w"><b>11</b></li><li class="w"><b>12</b></li>
      <li><i>20</i><b>13</b></li><li><b>14</b></li><li><b>15</b></li><li><b>16</b></li><li><b>17</b></li><li class="w"><b>18</b></li><li class="w"><b>19</b></li>
      <li><i>21</i><b>20</b></li><li><b>21</b></li><li><b>22</b></li><li><b>23</b></li><li><b>24</b></li><li class="w"><b>25</b></li><li class="w"><b>26</b></li>
      <li><i>22</i><b>27</b></li><li><b>28</b></li><li><b>29</b></li><li class="h"><b>30</b><small>Christi<br>Himmel<br>Fahrt</small></li><li><b>31</b></li>
    </ol>
  </section>

  <section class="month jun">
    <h2>JUNI</h2>
    <ol class="weekdays"><li>sa</li><li>so</li><li>mo</li><li>di</li><li>mi</li><li>do</li><li>fr</li><li>sa</li><li>so</li><li>mo</li><li>di</li><li>mi</li><li>do</li><li>fr</li><li>sa</li><li>so</li><li>mo</li><li>di</li><li>mi</li><li>do</li><li>fr</li><li>sa</li><li>so</li><li>mo</li><li>di</li><li>mi</li><li>do</li><li>fr</li><li>sa</li><li>so</li><li class="off">mo</li></ol>
    <ol class="days">
      <li class="w"><i>22</i><b>01</b></li><li class="w"><b>02</b></li>
      <li><i>23</i><b>03</b></li><li><b>04</b></li><li><b>05</b></li><li><b>06</b></li><li><b>07</b></li><li class="w"><b>08</b></li><li class="h"><b>09</b><small>Pfingst<br>Sonntag</small></li>
      <li class="h"><i>24</i><b>10</b><small>Pfingst<br>Montag</small></li><li><b>11</b></li><li><b>12</b></li><li><b>13</b></li><li><b>14</b></li><li class="w"><b>15</b></li><li class="w"><b>16</b></li>
      <li><i>25</i><b>17</b></li><li><b>18</b></li><li><b>19</b></li><li class="h"><b>20</b><small>Fron<br>Leichnam</small></li><li><b>21</b></li><li class="w"><b>22</b></li><li class="w"><b>23</b></li>
      <li><i>26</i><b>24</b></li><li><b>25</b></li><li><b>26</b></li><li><b>27</b></li><li><b>28</b></li><li class="w"><b>29</b></li><li class="w"><b>30</b></li>
      <li class="x"><i>27</i></li>
    </ol>
  </section>

  <p class="claim">Scannen und designen zahntechnischer<br>und zahnmedizinischer Arbeiten<br>Fräsen und 3D-Drucken von<br>in CAD konstruierten Objekten</p>

  <div class="mesh-visual" role="img" aria-label="Gitternetz-Darstellung eines CAD-Zahnmodells"></div>

  <div class="brand">
    <span class="brand-dot"></span>
    <div class="brand-name">Dentora</div>
    <div class="brand-sub">eine Gruppe der Norvak GmbH</div>
  </div>
</main>
</body>
</html>
```